Marcelo Quintana Postcard/Rack Card

Marcelo Quintana
Tenor & Vocal Coach
mqvoice@brivamail.com
(713) 582-6031
www.voicefromthecore.com
Want two sided postcard / rack card.4" x 9"
Front - vertical - picture in t-shirt, name, title (Tenor & Vocal Coach), contact information
Back - horizontal - picture in jacket, name, title (Tenor & Vocal Coach), contact information, bio (see attachment for words)
Do not leave space for an address.
Looking for an edgy modern design!

Target Market(s)

Young adults

Requirements
Nice to have
• Will pay extra to get a complimentary business card design, two sided

```html
<!DOCTYPE html>
<html lang="en">
<head>
<meta charset="utf-8">
<title>Marcelo Quintana – Rack Card</title>
<link rel="stylesheet" href="https://fonts.googleapis.com/css2?family=Graduate&family=Exo+2:wght@500&family=Roboto+Condensed:wght@400;700&display=swap">
<style>
  :root {
    --page: #ffffff;
    --charcoal: #2b2b2b;
    --ink: #111111;
    --red: #e02427;
    --white: #ffffff;
    --silver-light: #f4f4f4;
    --silver-mid: #c9c9c9;
    --silver-dark: #8d8d8d;
    --backdrop-light: #d4d1cc;
    --backdrop-dark: #4f4f4f;
    --subject-warm: #b89680;
    --subject-grey: #8e8e8e;
    --subject-denim: #3f4654;
  }
  * { margin: 0; padding: 0; box-sizing: border-box; }
  html, body {
    width: 696px; height: 1200px; overflow: hidden;
    background: var(--page);
  }
  .rack-card {
    position: absolute; left: 78px; top: 40px;
    width: 540px; height: 1120px;
    background: var(--charcoal);
    overflow: hidden;
  }
  .portrait {
    position: absolute; left: 0; top: 0; width: 540px; height: 700px;
    background:
      radial-gradient(ellipse at 50% 45%, var(--backdrop-light) 0%, #a3a19d 45%, var(--backdrop-dark) 100%);
  }
  .portrait-subject {
    position: absolute; left: 92px; top: 72px; width: 350px; height: 600px;
    border-radius: 175px 175px 24px 24px;
    background: linear-gradient(180deg,
      var(--subject-warm) 0%, var(--subject-warm) 28%,
      var(--subject-grey) 36%, var(--subject-grey) 82%,
      var(--subject-denim) 92%);
    box-shadow: -14px 10px 30px rgba(0,0,0,0.25);
    opacity: 0.9;
  }
  .bands { position: absolute; left: 0; top: 0; width: 540px; height: 1120px; }
  .name {
    position: absolute; left: 0; top: 716px; width: 544px;
    text-align: center;
    font-family: "Graduate", serif; font-weight: 400; font-size: 40px; line-height: 50px;
    color: var(--white); letter-spacing: 0.5px;
  }
  .role {
    position: absolute; left: 74px; top: 776px; width: 400px;
    text-align: center;
    font-family: "Exo 2", sans-serif; font-weight: 500; font-size: 27px; line-height: 36px;
    color: var(--white); letter-spacing: 1px;
  }
  .call-to-action {
    position: absolute; left: 69px; top: 893px;
    font-family: "Roboto Condensed", sans-serif; color: var(--ink);
  }
  .call-to-action .lead { font-weight: 700; font-size: 25px; line-height: 28px; }
  .call-to-action .push { font-size: 18px; letter-spacing: 1.6px; line-height: 26px; }
  .contact {
    position: absolute; right: 62px; top: 978px; text-align: right;
    font-family: "Exo 2", sans-serif; color: var(--white);
  }
  .contact p { display: flex; align-items: center; justify-content: flex-end; gap: 12px; }
  .contact .phone { font-size: 23px; letter-spacing: 1.5px; }
  .contact .email { font-size: 16px; margin-top: 2px; }
  .contact svg { fill: var(--red); }
</style>
</head>
<body>
  <main class="rack-card">
    <div class="portrait" role="img" aria-label="Photo of Marcelo Quintana smiling, in a grey t-shirt and jeans, against a grey faceted backdrop">
      <div class="portrait-subject" aria-hidden="true"></div>
    </div>

    <svg class="bands" viewBox="0 0 540 1120" aria-hidden="true">
      <defs>
        <linearGradient id="silver" x1="0" y1="0" x2="1" y2="0.3">
          <stop offset="0" stop-color="var(--silver-dark)"/>
          <stop offset="0.35" stop-color="var(--silver-light)"/>
          <stop offset="0.7" stop-color="var(--silver-mid)"/>
          <stop offset="1" stop-color="var(--silver-light)"/>
        </linearGradient>
        <linearGradient id="base" x1="0" y1="0" x2="0" y2="1">
          <stop offset="0" stop-color="#1c1c1c"/>
          <stop offset="1" stop-color="#3a3a3a"/>
        </linearGradient>
      </defs>
      <rect class="base" x="0" y="700" width="540" height="420" fill="url(#base)"/>
      <polygon class="band-red" points="0,700 120,652 540,652 540,862 0,832" fill="var(--red)"/>
      <polygon class="band-black" points="250,655 540,572 540,700" fill="var(--ink)"/>
      <polygon class="band-silver-top" points="0,622 540,548 540,578 0,702" fill="url(#silver)"/>
      <polygon class="title-tab" points="48,780 490,780 478,810 76,810" fill="var(--ink)"/>
      <polygon class="band-silver-bottom" points="0,830 540,868 540,958 0,985" fill="url(#silver)"/>
    </svg>

    <h1 class="name">MARCELO QUINTANA</h1>
    <p class="role">Tenor &amp; Vocal Coach</p>

    <div class="call-to-action">
      <p class="lead">For more information please</p>
      <p class="push">CONTACT MARCELO TODAY!</p>
    </div>

    <div class="contact">
      <p class="phone">(713) 582-6031
        <svg width="16" height="18" viewBox="0 0 16 18"><rect x="0" y="0" width="16" height="18" rx="2"/><path d="M5 4 q-2 5 3 10 l2-2 -2-2 q-1-2 0-3 z" fill="var(--charcoal)"/></svg>
      </p>
      <p class="email">mqvoice@brivamail.com
        <svg width="20" height="14" viewBox="0 0 20 14"><rect x="0" y="0" width="20" height="14" rx="1"/><path d="M1 1 L10 8 L19 1" stroke="var(--charcoal)" stroke-width="1.6" fill="none"/></svg>
      </p>
    </div>
  </main>
</body>
</html>
```